Cafe Opening Flyer Design Project

We need a flyer for the grand opening of our new cafe. It should appeal very much to our target consumer - working adults within the CBD area, where there is substantial competition as well.

Keep the message clear to the audience:
(below statements are just examples, please be creative and come up with your own phrases)
1. there's a new cafe you don't wanna miss out..
2. and coffee is always a good idea..

Be bold and creative!
Updates

Dear designers,

Kindly add in our opening hours on the flyer (A5 size, single side)
Weekdays: 7am to 6pm
Sat: 8am to 3pm
Closed on Sun & PH

Thank you!

Target Market(s)

Working adults in the CBD area, coffee lovers

Industry/Entity Type

Cafe

Requirements
Must have
• Location:
48 Brindlemoor Wharf, The Pavilion #05-14

```html
<!DOCTYPE html>
<html lang="en">
<head>
<meta charset="utf-8">
<title>Warmly Kept – A New Cafe</title>
<link rel="stylesheet" href="https://fonts.googleapis.com/css2?family=Oswald:wght@700&family=Permanent+Marker&family=Michroma&family=Playfair+Display:ital@1&display=block">
<style>
  :root {
    --espresso: #1a0d07;
    --roast: #3b1f12;
    --mocha: #8a5a3a;
    --cream: #e9e1c8;
    --bean: #4a1f0f;
    --ember: #f08a12;
    --milk: #ffffff;
    --caramel: #b07a2e;
  }
  html, body {
    margin: 0;
    padding: 0;
    width: 1200px;
    height: 927px;
    overflow: hidden;
    background: var(--espresso);
  }
  .flyer {
    position: relative;
    width: 1200px;
    height: 927px;
    overflow: hidden;
    background:
      radial-gradient(ellipse 420px 360px at 230px 170px, var(--cream) 0%, #bfae8e 30%, var(--mocha) 60%, transparent 85%),
      linear-gradient(160deg, #a87c58 0%, #6b4128 45%, var(--roast) 70%, var(--espresso) 100%);
  }
  .cup-photo {
    position: absolute;
    left: 560px;
    top: 0;
    width: 640px;
    height: 927px;
    background:
      radial-gradient(ellipse 230px 140px at 405px 235px, #f2b06a 0%, #d97a30 55%, transparent 100%),
      radial-gradient(ellipse 300px 260px at 400px 330px, #7a2c12 0%, #3a150a 70%, transparent 100%),
      linear-gradient(90deg, transparent 0%, rgba(20,10,6,0.6) 25%, var(--espresso) 100%);
  }
  .brand {
    position: absolute;
    left: 120px;
    top: 130px;
    display: flex;
    align-items: center;
    gap: 16px;
  }
  .brand-dot {
    width: 22px;
    height: 22px;
    border-radius: 50%;
    background: var(--caramel);
  }
  .brand-name {
    font-family: "Playfair Display", serif;
    font-style: italic;
    font-size: 62px;
    line-height: 1;
    color: var(--bean);
    white-space: nowrap;
  }
  .tagline {
    position: absolute;
    font-family: "Oswald", sans-serif;
    font-weight: 700;
    color: var(--bean);
    text-shadow: 0 0 10px rgba(255,230,170,0.8), 0 0 3px rgba(255,230,170,0.9);
    transform-origin: left bottom;
    line-height: 1;
    margin: 0;
    white-space: nowrap;
  }
  .tagline-coffee {
    left: 152px;
    top: 318px;
    font-size: 78px;
    transform: rotate(-8deg);
  }
  .tagline-idea {
    left: 60px;
    top: 470px;
    font-size: 84px;
    transform: rotate(-11deg);
  }
  .callout {
    position: absolute;
    left: 488px;
    top: 530px;
    margin: 0;
    font-family: "Permanent Marker", "Oswald", sans-serif;
    font-size: 76px;
    line-height: 1;
    color: var(--ember);
    transform: rotate(-13deg);
    transform-origin: left bottom;
    white-space: nowrap;
  }
  .headline {
    position: absolute;
    left: 0;
    width: 1200px;
    top: 590px;
    margin: 0;
    text-align: center;
    font-family: "Permanent Marker", "Oswald", sans-serif;
    font-weight: 400;
    font-size: 196px;
    line-height: 1.1;
    letter-spacing: 2px;
    color: var(--milk);
    text-shadow: 0 0 8px rgba(0,0,0,0.8);
    white-space: nowrap;
  }
  .location {
    position: absolute;
    left: 0;
    width: 1200px;
    top: 850px;
    margin: 0;
    text-align: center;
    font-family: "Michroma", sans-serif;
    font-size: 21px;
    letter-spacing: 2px;
    color: var(--milk);
    text-transform: uppercase;
    white-space: nowrap;
  }
  .hours {
    position: absolute;
    left: 0;
    width: 1200px;
    top: 890px;
    margin: 0;
    text-align: center;
    font-family: "Michroma", sans-serif;
    font-size: 14px;
    letter-spacing: 1px;
    color: var(--ember);
    text-transform: uppercase;
    white-space: nowrap;
  }
</style>
</head>
<body>
  <main class="flyer">
    <div class="cup-photo" role="img" aria-label="Photograph of a cup of frothy espresso on a coffee machine drip tray"></div>

    <div class="brand">
      <span class="brand-dot"></span>
      <span class="brand-name">Warmly Kept</span>
    </div>

    <p class="tagline tagline-coffee">Coffee</p>
    <p class="tagline tagline-idea">is&nbsp; a Good idea..</p>

    <p class="callout">DON'T MISS OUT..</p>

    <h1 class="headline">A NEW CAFE</h1>

    <p class="location">Location: 48 Brindlemoor Wharf, The Pavilion #05-14</p>
    <p class="hours">Weekdays 7am – 6pm &nbsp;·&nbsp; Sat 8am – 3pm &nbsp;·&nbsp; Closed Sun &amp; PH</p>
  </main>
</body>
</html>
```